Website Header Design

Hi,

We're an electrical company that is looking for a new website header.
Our website is www.brambletonwiring.com
We are located in Toronto, Ontario, Canada.
We perform a lot of high rise electrical service work, snow melting system installation in garage ramps, and other general electrical work.
We're willing to change the size of the header and location/look of menus if needed but it is not required. We are hoping to keep our slogan if possible but having it in the header is not a make or break item. Whatever looks better.

Maybe the Toronto skyline could be incorporated somehow but the header also has to have some relevance to an electrical company.
I uploaded png files of the logo but I also have vector files available if needed

Target Market(s)

Property Managers, Contractors, Consulting Engineers

Industry/Entity Type

Electrical

Requirements
Must have
• Our Logo.
Nice to have
• Slogan
Should not have
• Flash

```html
<!DOCTYPE html>
<html lang="en">
<head>
<meta charset="utf-8">
<title>Brambleton Wiring – Header</title>
<link rel="stylesheet" href="https://fonts.googleapis.com/css2?family=Arimo:wght@400;600&display=swap">
<style>
  :root {
    --page-white: #ffffff;
    --band-black: #050505;
    --band-charcoal: #1a1a1a;
    --accent-orange: #f29a2e;
    --glow-orange: rgba(229, 118, 31, 0.28);
    --glow-grey: rgba(190, 190, 190, 0.30);
    --button-top: #8a8a8a;
    --button-mid: #585858;
    --button-bottom: #363636;
    --text-white: #ffffff;
  }
  * { margin: 0; padding: 0; box-sizing: border-box; }
  html, body {
    width: 1200px;
    height: 270px;
    overflow: hidden;
    background: var(--page-white);
    font-family: "Arimo", Arial, sans-serif;
  }
  .site-header {
    position: relative;
    width: 1200px;
    height: 270px;
  }
  .header-band {
    position: absolute;
    left: 0;
    top: 23px;
    width: 1172px;
    height: 247px;
    background: linear-gradient(180deg, var(--band-black) 0%, var(--band-charcoal) 55%, var(--band-black) 100%);
    overflow: hidden;
  }
  .network-glow {
    position: absolute;
    left: 720px;
    top: 0;
    width: 452px;
    height: 200px;
    background: radial-gradient(ellipse at 65% 35%, var(--glow-grey) 0%, rgba(120,120,120,0.14) 45%, rgba(0,0,0,0) 75%);
  }
  .energy-glow {
    position: absolute;
    left: 200px;
    top: 60px;
    width: 940px;
    height: 140px;
    background: radial-gradient(ellipse at 50% 50%, var(--glow-orange) 0%, rgba(229,118,31,0.10) 45%, rgba(0,0,0,0) 72%);
  }
  .brand {
    position: absolute;
    left: 14px;
    top: 38px;
    width: 196px;
    text-align: center;
  }
  .brand-mark {
    display: block;
    width: 64px;
    height: 64px;
    margin: 0 auto 34px;
    background: var(--accent-orange);
  }
  .brand-name {
    color: var(--text-white);
    font-weight: 600;
    font-size: 27px;
    line-height: 1.12;
  }
  .main-nav {
    position: absolute;
    left: 264px;
    top: 184px;
    display: flex;
    gap: 17px;
  }
  .nav-button {
    display: flex;
    align-items: center;
    justify-content: center;
    width: 130px;
    height: 50px;
    border-radius: 8px;
    background: linear-gradient(180deg, var(--button-top) 0%, var(--button-mid) 45%, var(--button-bottom) 100%);
    box-shadow: 0 0 8px rgba(255,255,255,0.25), inset 0 1px 0 rgba(255,255,255,0.35);
    color: var(--text-white);
    font-size: 28px;
    letter-spacing: -1.8px;
    white-space: nowrap;
    text-decoration: none;
    text-shadow: 0 1px 3px rgba(0,0,0,0.7);
  }
</style>
</head>
<body>
<header class="site-header">
  <div class="header-band">
    <div class="network-glow" role="img" aria-label="Glowing network of connected nodes suggesting an electrical grid"></div>
    <div class="energy-glow" role="img" aria-label="Flowing orange energy wave crossing the header"></div>
    <div class="brand">
      <span class="brand-mark"></span>
      <p class="brand-name">Brambleton<br>Wiring</p>
    </div>
    <nav class="main-nav">
      <a class="nav-button" href="#">Home</a>
      <a class="nav-button" href="#">About us</a>
      <a class="nav-button" href="#">Services</a>
      <a class="nav-button" href="#">Projects</a>
      <a class="nav-button" href="#">Clients</a>
      <a class="nav-button" href="#">Contact us</a>
    </nav>
  </div>
</header>
</body>
</html>
```